Business Card Design for Occupational Medicine Start Up Company

We need to design a professional business card. We are a healthcare company providing occupational medicine services to blue collar industries. We are professional, efficient and high quality service providers.

Target Market(s)

Blue Collar Industry: Shipbuilding, Ports, Trucking Companies; The Executives and Safety Officers for these companies

Industry/Entity Type

Healthcare

Contact Information for Business Card

Logo, Name, Title, Email, Phone

Other font styles liked:
• Please match our Brand Guide

Requirements
Must have
• Our Company Colors and Logo

```html
<!DOCTYPE html>
<html lang="en">
<head>
<meta charset="utf-8">
<title>CrewWell Business Card</title>
<link rel="stylesheet" href="https://fonts.googleapis.com/css2?family=Montserrat:wght@500;700&family=Open+Sans:wght@400;600&display=swap">
<style>
  :root {
    --navy: #0f1660;
    --navy-deep: #0b0f4a;
    --sky: #5cc3ee;
    --gold: #f2b51c;
    --orange: #f08a1d;
    --paper: #fbfbfb;
    --backdrop: #454b4d;
    --white: #ffffff;
  }
  * { margin: 0; padding: 0; box-sizing: border-box; }
  html, body { width: 1200px; height: 960px; overflow: hidden; }
  body { background: var(--backdrop); position: relative; font-family: "Open Sans", Arial, sans-serif; }

  .card {
    position: absolute;
    width: 560px; height: 320px;
    border-radius: 28px;
    overflow: hidden;
    background: var(--paper);
    box-shadow: 0 12px 30px rgba(0,0,0,.35);
  }
  .card-front { left: 60px; top: 110px; }
  .card-back { left: 580px; top: 520px; }
  .card svg.card-shapes { position: absolute; inset: 0; }

  .brand {
    position: absolute;
    display: flex; align-items: center; gap: 12px;
    font-family: "Montserrat", Arial, sans-serif;
    font-weight: 700;
    color: var(--navy);
    letter-spacing: 1px;
  }
  .brand-dot { border-radius: 50%; background: var(--gold); flex: none; }
  .card-front .brand { left: 90px; top: 100px; font-size: 46px; }
  .card-front .brand-dot { width: 30px; height: 30px; }
  .card-back .brand { left: 26px; top: 140px; font-size: 32px; }
  .card-back .brand-dot { width: 22px; height: 22px; }

  .front-url {
    position: absolute; left: 280px; top: 250px;
    color: var(--white); font-size: 15px; letter-spacing: .5px;
  }

  .holder { position: absolute; left: 330px; top: 48px; padding-left: 16px; }
  .holder::before {
    content: ""; position: absolute; left: 0; top: 4px;
    width: 3px; height: 50px; background: var(--orange);
  }
  .holder-name {
    font-family: "Montserrat", Arial, sans-serif; font-weight: 500;
    color: var(--sky); font-size: 24px; letter-spacing: .5px;
  }
  .holder-title { color: var(--white); font-size: 15px; margin-top: 2px; }

  .contacts { position: absolute; left: 336px; top: 150px; list-style: none; }
  .contacts li { display: flex; align-items: center; gap: 14px; height: 46px; color: var(--white); font-size: 15px; }
  .contact-icon {
    width: 34px; height: 34px; border-radius: 50%;
    border: 2px solid var(--white); background: var(--navy-deep);
    display: flex; align-items: center; justify-content: center; flex: none;
  }
</style>
</head>
<body>

<section class="card card-front" aria-label="Card front">
  <svg class="card-shapes" width="560" height="320" viewBox="0 0 560 320" aria-hidden="true">
    <rect x="478" y="0" width="12" height="220" fill="var(--sky)"/>
    <rect x="496" y="0" width="14" height="220" fill="var(--navy)"/>
    <rect x="520" y="0" width="40" height="220" fill="var(--gold)"/>
    <rect x="510" y="0" width="10" height="220" fill="var(--paper)"/>
    <path d="M0 296 C 110 296 150 300 158 270 C 168 236 190 226 230 226 L 360 226 C 400 226 410 196 446 196 L 560 196 L 560 320 L 0 320 Z" fill="var(--navy)"/>
  </svg>
  <div class="brand"><span class="brand-dot"></span><span class="brand-name">CREWWELL</span></div>
  <p class="front-url">www.crewwell.com</p>
</section>

<section class="card card-back" aria-label="Card back">
  <svg class="card-shapes" width="560" height="320" viewBox="0 0 560 320" aria-hidden="true">
    <path d="M200 0 C 290 20 330 140 300 320 L 560 320 L 560 0 Z" fill="var(--navy)"/>
    <path d="M200 0 C 290 20 330 140 300 320" fill="none" stroke="var(--gold)" stroke-width="4"/>
  </svg>
  <div class="brand"><span class="brand-dot"></span><span class="brand-name">CREWWELL</span></div>

  <div class="holder">
    <p class="holder-name">MARTEN HALE</p>
    <p class="holder-title">Chief Executive Officer</p>
  </div>

  <ul class="contacts">
    <li>
      <span class="contact-icon">
        <svg width="16" height="16" viewBox="0 0 24 24" aria-hidden="true"><path d="M6.6 10.8a15 15 0 0 0 6.6 6.6l2.2-2.2c.3-.3.7-.4 1-.2 1.1.4 2.3.6 3.6.6.6 0 1 .4 1 1V20c0 .6-.4 1-1 1C10.6 21 3 13.4 3 4c0-.6.4-1 1-1h3.5c.6 0 1 .4 1 1 0 1.3.2 2.5.6 3.6.1.3 0 .7-.2 1z" fill="#fff"/></svg>
      </span>
      <span>732-555-0148</span>
    </li>
    <li>
      <span class="contact-icon">
        <svg width="16" height="16" viewBox="0 0 24 24" aria-hidden="true"><rect x="7" y="2" width="10" height="20" rx="2" fill="none" stroke="#fff" stroke-width="2"/><circle cx="12" cy="18" r="1" fill="#fff"/></svg>
      </span>
      <span>732-555-0172</span>
    </li>
    <li>
      <span class="contact-icon" style="font-weight:600;font-size:16px;">@</span>
      <span>hello@crewwell.com</span>
    </li>
  </ul>
</section>

</body>
</html>
```